Business Card Design Project

New Private residential substance abuse treatment facility in Mapleton, UT. Facility located in elegant 11,000 home with stunning views of the mountains. Wish to incorporate colored logo. Business name- Birchwell Harbor Wellness. Facility is Tudor style with traditional furnishings, an overhead picture is attached. Lettering in a simple scroll or old english style. Must be easy to read with clear moderetly large font.
Updates

It seems the project time frame listed was not correct- it is a week.

Target Market(s)

Adults 18 and over with substance abuse issues requiring residential rehabilitation. Referral base are medical/mental health professionals, families and community agencies.

Industry/Entity Type

Residential

Colors
9bcb3b
fece3e
fbee3f

Requirements
Must have
• Clear and easy to read, professional and upscale presentation. Need logo, name, title, address, phone, fax and web page address. May add slogan later. Use same font as logo.
Nice to have
• Logo has a green mountain and a gold maple leaf so a nature themed element may work. Want to promote peaceful grounded image. Logo attached.
Should not have
• No tiny or complicated font. No modern or tech looking images. No light colored fonts.

```html
<!DOCTYPE html>
<html lang="en">
<head>
<meta charset="utf-8">
<title>Birchwell Harbor Wellness – Business Card</title>
<link rel="stylesheet" href="https://fonts.googleapis.com/css2?family=Crimson+Text:wght@400;600;700&display=swap">
<style>
  :root {
    --page-bg: #e9e9e9;
    --card-white: #ffffff;
    --card-fade: #eeeeee;
    --frame-dark: #3a3a3a;
    --ink: #2e2e2e;
    --title-green: #4f7a2b;
    --icon-gold: #d9a02c;
  }
  * { margin: 0; padding: 0; box-sizing: border-box; }
  html, body {
    width: 1200px;
    height: 900px;
    overflow: hidden;
    background: var(--page-bg);
  }
  .business-card {
    position: absolute;
    left: 75px;
    top: 150px;
    width: 1050px;
    height: 600px;
    background: var(--card-white);
    padding: 16px;
    box-shadow: 0 6px 18px rgba(0,0,0,0.12);
  }
  .card-frame {
    position: relative;
    width: 100%;
    height: 100%;
    border: 14px solid var(--frame-dark);
    background: linear-gradient(160deg, var(--card-white) 35%, var(--card-fade) 100%);
    font-family: "Crimson Text", Georgia, serif;
    color: var(--ink);
  }
  .contact-person {
    position: absolute;
    right: 34px;
    top: 26px;
    text-align: right;
    line-height: 1.2;
  }
  .person-name {
    font-size: 27px;
    font-weight: 600;
  }
  .person-title {
    font-size: 20px;
    font-weight: 700;
    color: var(--title-green);
  }
  .brand-name {
    position: absolute;
    left: 0;
    right: 0;
    top: 190px;
    padding-left: 140px;
    text-align: center;
    font-size: 56px;
    font-weight: 400;
    color: var(--ink);
    letter-spacing: 0.5px;
  }
  .contact-list {
    position: absolute;
    left: 40px;
    bottom: 30px;
    list-style: none;
    font-size: 29px;
    font-weight: 600;
    line-height: 40px;
  }
  .contact-list li {
    display: flex;
    align-items: center;
    gap: 10px;
  }
  .contact-list li.continued { padding-left: 40px; }
  .contact-icon {
    width: 30px;
    height: 30px;
    flex: none;
    fill: var(--icon-gold);
  }
</style>
</head>
<body>
  <div class="business-card">
    <div class="card-frame">
      <div class="contact-person">
        <div class="person-name">Dana Ellery</div>
        <div class="person-title">Manager</div>
      </div>

      <div class="brand-name">Birchwell Harbor Wellness</div>

      <ul class="contact-list">
        <li>
          <svg class="contact-icon" viewBox="0 0 24 24" aria-hidden="true"><path d="M6.6 10.8a15.2 15.2 0 0 0 6.6 6.6l2.2-2.2a1 1 0 0 1 1-.25 11.4 11.4 0 0 0 3.6.57 1 1 0 0 1 1 1V20a1 1 0 0 1-1 1A17 17 0 0 1 3 4a1 1 0 0 1 1-1h3.5a1 1 0 0 1 1 1c0 1.25.2 2.45.57 3.57a1 1 0 0 1-.25 1z"/></svg>
          <span class="phone">719-555-0142</span>
        </li>
        <li>
          <svg class="contact-icon" viewBox="0 0 24 24" aria-hidden="true"><rect x="6" y="2" width="12" height="7" rx="1"/><rect x="3" y="9" width="18" height="10" rx="2"/><rect x="7" y="15" width="10" height="7" rx="1" fill="#fff"/><rect x="8.5" y="17" width="7" height="1.2" rx=".6"/><rect x="8.5" y="19.3" width="7" height="1.2" rx=".6"/></svg>
          <span class="fax">719-555-0178</span>
        </li>
        <li>
          <svg class="contact-icon" viewBox="0 0 24 24" aria-hidden="true"><rect x="2" y="5" width="20" height="14" rx="2"/><path d="M3 6.5l9 6.5 9-6.5" fill="none" stroke="#fff" stroke-width="1.8"/></svg>
          <span class="email">birchwellharbor@mailbox.com</span>
        </li>
        <li>
          <svg class="contact-icon" viewBox="0 0 24 24" aria-hidden="true"><circle cx="12" cy="12" r="10"/><g fill="none" stroke="#fff" stroke-width="1.4"><ellipse cx="12" cy="12" rx="4.2" ry="9.6"/><path d="M2.5 12h19M4 7h16M4 17h16"/></g></svg>
          <span class="website">www.birchwellharbor.com</span>
        </li>
        <li>
          <svg class="contact-icon" viewBox="0 0 24 24" aria-hidden="true"><path d="M12 2.5 1.5 12h3v9.5h6v-6h3v6h6V12h3z"/></svg>
          <span class="address-line">4820 N. Linden Ridge Road,</span>
        </li>
        <li class="continued">
          <span class="address-line">Alder Falls, CO 80911</span>
        </li>
      </ul>
    </div>
  </div>
</body>
</html>
```